Customizable Gift Note Card Design

I need a gift note card designed for my Healthy Snacks Care Package company. I need to be able to customize each card with the customer's gift message to the recipient and print to a standard printer.

The card should be single-sided 5 x 7, include our logo, keep colors and graphics simple since they will be printed for each individual order on a standard printer. I would like the following quote to be included in a small and subtle way: "Food is symbolic of love when words are inadequate." —Bertram K. Osslund. Our website thebrightpantrybites.example should also be included.

I have included pictures of our product packaging for reference.

Target Market(s)

Gift recipients: Students, people recovering from illness, housewarming, thank you gifts...etc.

Industry/Entity Type

It Company

Colors

Designer to choose colors to be used in the design.

Requirements
Must have
• We are looking for a simple, cute and elegant gift card that reflects our branding. Must be customizable and printable on a standard printer.
• Must be single-sided 5x7.

```html
<!DOCTYPE html>
<html lang="en">
<head>
<meta charset="UTF-8">
<title>The Bright Pantry – Gift Card</title>
<link rel="stylesheet" href="https://fonts.googleapis.com/css2?family=Quicksand:wght@400;500;600;700&display=swap">
<style>
  :root {
    --backdrop: #d9d7d3;
    --paper: #efedea;
    --ink: #3b3634;
    --ink-soft: #4a4441;
    --rust: #b65f3c;
    --charcoal: #2f2b29;
  }
  * { margin: 0; padding: 0; box-sizing: border-box; }
  html, body {
    width: 1200px;
    height: 900px;
    overflow: hidden;
    background: var(--backdrop);
  }
  body {
    position: relative;
    font-family: "Quicksand", sans-serif;
    color: var(--ink);
  }
  .gift-card {
    position: absolute;
    left: 110px;
    top: 100px;
    width: 980px;
    height: 700px;
    background: var(--paper);
    box-shadow: 0 10px 30px rgba(0,0,0,0.18);
    overflow: hidden;
  }
  .mascot-illustration {
    position: absolute;
    left: 0;
    top: 0;
    width: 350px;
    height: 500px;
    background:
      linear-gradient(180deg, var(--charcoal) 0%, var(--charcoal) 30%, var(--rust) 48%, var(--charcoal) 68%, var(--ink-soft) 100%);
    border-radius: 0 0 160px 0;
    opacity: 0.9;
  }
  .brand {
    position: absolute;
    right: 70px;
    top: 70px;
    text-align: right;
  }
  .brand-name {
    font-size: 36px;
    font-weight: 600;
    color: var(--ink);
    letter-spacing: 0.5px;
  }
  .card-title {
    margin-top: 14px;
    font-size: 32px;
    font-weight: 500;
    color: var(--rust);
    letter-spacing: 1px;
  }
  .gift-message {
    position: absolute;
    right: 70px;
    top: 250px;
    width: 560px;
    text-align: right;
    font-size: 29px;
    line-height: 1.38;
    font-weight: 500;
    color: var(--ink);
  }
  .quote {
    position: absolute;
    left: 170px;
    top: 560px;
    width: 360px;
    font-size: 19px;
    line-height: 1.3;
    color: var(--rust);
  }
  .quote-author {
    display: block;
    font-weight: 700;
  }
  .website {
    position: absolute;
    right: 70px;
    bottom: 76px;
    font-size: 26px;
    font-weight: 500;
    color: var(--ink);
  }
</style>
</head>
<body>
  <main class="gift-card">
    <div class="mascot-illustration" role="img" aria-label="Illustration of a gentleman mascot with bowler hat, rust-coloured glasses, moustache and bow tie"></div>

    <header class="brand">
      <div class="brand-name">The Bright Pantry</div>
      <div class="card-title">GIFT CARD</div>
    </header>

    <p class="gift-message">Lorem ipsum dolor sit amet, consectetuer adipiscing elit. Ulioson commodo ligula eget dolor. Aenean massa.</p>

    <blockquote class="quote">
      “Food is symbolic of love when words are inadequate.”
      <span class="quote-author">– Bertram K. Osslund</span>
    </blockquote>

    <div class="website">thebrightpantrybites.example</div>
  </main>
</body>
</html>
```